Summit Brightway Realty Group & Greenleaf Lending Services, Inc.
Present Our
Annual Holiday Celebration

for Agents, Originators, Clients & Friends
All are Welcome!!

Catered by Chef Ramo Ramo
w/ DJ and Full Dance Floor

** No Cover Charge
Saturday, January 22, 2022
7 pm - 11 pm

at Velvet Parlor
4871 Q Street NE Washington DC 20019

Call Marcus Pelletier at (240) 555-0184 with questions.

```html
<!DOCTYPE html>
<html lang="en">
<head>
<meta charset="utf-8">
<title>Annual Holiday Celebration</title>
<link rel="stylesheet" href="https://fonts.googleapis.com/css2?family=Great+Vibes&family=Montserrat:wght@400;500;600;700&display=swap">
<style>
  :root {
    --artboard: #5f5f5f;
    --navy-deep: #0a2566;
    --navy: #103a8a;
    --navy-glow: #2a6cc4;
    --gold: #c9a94a;
    --gold-light: #f1e2a0;
    --gold-dark: #a8892c;
    --ink-blue: #14509a;
    --paper: #ffffff;
    --paper-shade: #eceff3;
    --text-dark: #1f2a3a;
  }
  * { margin: 0; padding: 0; box-sizing: border-box; }
  html, body {
    width: 1200px; height: 1170px; overflow: hidden;
    background: var(--artboard);
  }
  .flyer {
    position: absolute; left: 150px; top: 158px;
    width: 907px; height: 907px; overflow: hidden;
    background: linear-gradient(180deg, var(--paper) 60%, var(--paper-shade) 100%);
    font-family: "Montserrat", sans-serif;
  }
  .flyer__backdrop { position: absolute; inset: 0; width: 907px; height: 907px; }
  .confetti {
    position: absolute; left: 0; top: 0; width: 907px; height: 110px;
    background: linear-gradient(180deg, rgba(230,200,110,.85) 0%, rgba(215,190,120,.45) 45%, rgba(16,58,138,0) 100%);
  }
  .hosts {
    position: absolute; top: 116px; left: 0; width: 100%;
    text-align: center; color: var(--paper);
    font-weight: 600; font-size: 17px; letter-spacing: .2px;
  }
  .ribbon {
    position: absolute; left: 300px; top: 166px; width: 307px; height: 40px;
    background: linear-gradient(90deg, var(--gold-dark), var(--gold-light) 50%, var(--gold-dark));
    clip-path: polygon(0 0, 100% 0, 94% 50%, 100% 100%, 0 100%, 6% 50%);
    color: var(--paper); font-weight: 700; font-size: 21px; letter-spacing: .5px;
    display: flex; align-items: center; justify-content: center;
  }
  .title {
    position: absolute; top: 222px; left: 0; width: 100%; text-align: center;
    font-family: "Great Vibes", cursive; font-size: 88px; line-height: 1.2;
    color: var(--gold-light);
  }
  .audience {
    position: absolute; top: 353px; left: 0; width: 100%; text-align: center;
    color: var(--paper); font-size: 20px; font-weight: 500;
  }
  .headline {
    position: absolute; left: 0; width: 100%; text-align: center;
    color: var(--gold); font-weight: 700; font-size: 27px;
  }
  .headline--date { top: 425px; }
  .headline--venue { top: 466px; }
  .portrait-ring {
    position: absolute; left: 27px; top: 481px; width: 246px; height: 246px;
    border-radius: 50%; background: linear-gradient(135deg, var(--gold-light), var(--gold-dark));
  }
  .portrait {
    position: absolute; left: 13px; top: 13px; width: 220px; height: 220px;
    border-radius: 50%; border: 4px solid var(--paper);
    background: radial-gradient(circle at 50% 40%, #d9d6d0 0%, #9e958b 55%, #4b4038 100%);
  }
  .catering {
    position: absolute; left: 330px; top: 570px; width: 270px;
    text-align: center; color: var(--paper); font-size: 15px; line-height: 1.45; font-weight: 500;
  }
  .details {
    position: absolute; left: 43px; top: 768px;
    color: var(--ink-blue); font-size: 15px; line-height: 22px;
  }
  .details strong { font-weight: 700; }
  .details .address { color: var(--text-dark); }
  .contact-band {
    position: absolute; left: 0; top: 864px; width: 560px; height: 29px;
    background: linear-gradient(90deg, var(--gold) 0%, var(--gold) 70%, rgba(241,226,160,.5) 100%);
    color: var(--paper); font-size: 16px; font-weight: 500;
    padding-left: 43px; display: flex; align-items: center;
  }
  .contact-band strong { font-weight: 700; margin: 0 4px; }
  .brand {
    position: absolute; display: flex; align-items: center; gap: 8px;
    color: var(--ink-blue); font-weight: 700;
  }
  .brand--realty { left: 420px; top: 795px; width: 150px; font-size: 13px; line-height: 1.25; }
  .brand__square { flex: none; width: 14px; height: 14px; background: var(--ink-blue); }
  .brand--lending { left: 600px; top: 735px; width: 280px; font-size: 17px; line-height: 1.3; }
  .brand__circle { flex: none; width: 70px; height: 70px; border-radius: 50%; background: var(--gold-light); }
</style>
</head>
<body>
  <main class="flyer">
    <svg class="flyer__backdrop" viewBox="0 0 907 907" aria-hidden="true">
      <defs>
        <radialGradient id="nightBlue" cx="0.62" cy="0.62" r="0.75">
          <stop offset="0" stop-color="var(--navy-glow)"/>
          <stop offset="0.5" stop-color="var(--navy)"/>
          <stop offset="1" stop-color="var(--navy-deep)"/>
        </radialGradient>
        <linearGradient id="goldBand" x1="0" y1="0" x2="1" y2="0">
          <stop offset="0" stop-color="#a8892c"/>
          <stop offset="0.5" stop-color="#d9bf64"/>
          <stop offset="1" stop-color="#a8892c"/>
        </linearGradient>
      </defs>
      <path d="M0,0 H907 V520 C880,740 600,760 330,690 C200,650 80,520 0,418 Z" fill="url(#nightBlue)"/>
      <path d="M907,520 C880,740 600,760 330,690 C200,650 80,520 0,418" fill="none" stroke="url(#goldBand)" stroke-width="14"/>
    </svg>

    <div class="confetti" role="img" aria-label="Gold and white confetti sparkles with small stars along the top edge"></div>

    <p class="hosts">SUMMIT BRIGHTWAY REALTY GROUP &amp; GREENLEAF LENDING SERVICES, INC.</p>
    <div class="ribbon">PRESENT OUR</div>
    <h1 class="title">Annual Holiday Celebration</h1>
    <p class="audience">for Agents, Originators, Clients &amp; Friends, all are Welcome!!</p>
    <p class="headline headline--date">JANUARY 22. FROM 7 PM - 11 PM</p>
    <p class="headline headline--venue">VELVET PARLOR</p>

    <div class="portrait-ring">
      <div class="portrait" role="img" aria-label="Portrait photo of Chef Ramo Ramo in a chef's jacket"></div>
    </div>

    <p class="catering">Catered by Chef Ramo Ramo<br>w/ DJ and Full Dance Floor</p>

    <div class="details">
      <strong>Saturday, January 22, 2022</strong><br>
      from 7 pm - 11 pm<br>
      <strong>at Velvet Parlor</strong><br>
      <span class="address">4871 Q Street NE Washington DC 20019</span>
    </div>

    <div class="brand brand--realty">
      <span class="brand__square"></span>
      <span>Summit Brightway Realty Group</span>
    </div>

    <div class="brand brand--lending">
      <span class="brand__circle"></span>
      <span>Greenleaf Lending Services, Inc.</span>
    </div>

    <div class="contact-band">Call Marcus Pelletier at <strong>(240) 555-0184</strong> with questions.</div>
  </main>
</body>
</html>
```